Autohaus sucht Visitenkarten
Zielgruppe
Verkauf und Reparatur von PKW
Zielgruppe ist jeder Autofahrer/in
Aufgabenstellung
Erstellen eines Visitenkartendesigns mit stilisiertem Auto als Logo, eher modern gestaltet, ohne Schnörkel, zweifarbig, Anthrazit sollte im Logo enthalten sein.

```html
<!DOCTYPE html>
<html lang="de">
<head>
<meta charset="utf-8">
<title>Autohaus Brenning – Visitenkarte</title>
<link href="https://fonts.googleapis.com/css2?family=Black+Ops+One&family=Roboto:wght@400&display=swap" rel="stylesheet">
<style>
  :root {
    --anthracite: #2b2b2d;
    --signal-red: #e3151b;
    --card-white: #ffffff;
    --backdrop: #e9e7e3;
  }
  html, body {
    margin: 0;
    width: 1200px;
    height: 900px;
    overflow: hidden;
    background: var(--backdrop);
  }
  .business-card {
    position: absolute;
    left: 341px;
    top: 50px;
    width: 518px;
    height: 800px;
    background: var(--card-white);
    box-shadow: 0 6px 24px rgba(0,0,0,0.12);
    overflow: hidden;
  }
  .brand {
    position: absolute;
    top: 170px;
    left: 0;
    width: 100%;
    display: flex;
    justify-content: center;
    align-items: center;
    gap: 14px;
  }
  .brand-mark {
    width: 22px;
    height: 22px;
    background: var(--signal-red);
  }
  .brand-name {
    font-family: "Black Ops One", sans-serif;
    font-size: 34px;
    letter-spacing: 1px;
    color: var(--anthracite);
    text-transform: uppercase;
  }
  .contact-person {
    position: absolute;
    top: 275px;
    right: 70px;
    text-align: right;
  }
  .person-name {
    font-family: "Black Ops One", sans-serif;
    font-size: 42px;
    letter-spacing: 2px;
    color: var(--anthracite);
    text-transform: uppercase;
    margin: 0;
  }
  .person-role {
    font-family: "Black Ops One", sans-serif;
    font-size: 20px;
    color: var(--signal-red);
    text-transform: uppercase;
    margin: 6px 0 0;
  }
  .address {
    position: absolute;
    top: 440px;
    right: 70px;
    text-align: right;
    font-family: "Black Ops One", sans-serif;
    font-size: 19px;
    line-height: 1.25;
    color: var(--anthracite);
    text-transform: uppercase;
    font-style: normal;
  }
  .swoosh {
    position: absolute;
    left: 0;
    top: 520px;
    width: 518px;
    height: 220px;
  }
  .phone {
    position: absolute;
    right: 40px;
    bottom: 36px;
    font-family: "Roboto", sans-serif;
    font-size: 26px;
    color: var(--signal-red);
    margin: 0;
  }
</style>
</head>
<body>
  <section class="business-card">
    <div class="brand">
      <span class="brand-mark"></span>
      <span class="brand-name">Autohaus Brenning</span>
    </div>

    <div class="contact-person">
      <p class="person-name">Jonas Vell</p>
      <p class="person-role">Manager</p>
    </div>

    <address class="address">
      Am Lindenhof 4<br>
      14972 Wiesenau, OT Roth
    </address>

    <svg class="swoosh" viewBox="0 0 518 220" aria-hidden="true">
      <path fill="var(--signal-red)"
            d="M0 200 C120 150 260 110 360 60 C420 32 470 12 505 0
               C480 24 430 56 370 88 C270 140 140 180 0 216 Z"/>
    </svg>

    <p class="phone">Tel. 033845/41873</p>
  </section>
</body>
</html>
```